PERMITRONICS: "THE ART OF PERMITS"

WE NEED A SIMPLE MODERN WEBSITE THAT EXPLAINS THE FIRM SERVICES OF HELPING PEOPLE WITH ALL THINGS RELATED TO FLORIDA STATE LICENSING IN THE USA (STATE LICENSES FOR BUILDERS AND ELECTRICIANS). WE HANDLE INIITIAL APPLICATION FOR LICENSURE, ADDITIONAL LICENSURE FOR THEIR SECOND OR THIRD COMPANIES, WE DEFEND PEOPLE WHO HAVE COMPLAINTS AGAINST THEIR LICENSE, HELP THEM WHILE ON LICENSE PROBATION, HELP THEM TERMINATE PROBATION, HELP THEM WITH CONTINUING EDUCATION SERVICES TO MAINTAIN THEIR LICENSE, AND WE HELP BROKER LICENSURE FOR PEOPLE LOOKING FOR A LICENSED PERSON TO LICENSE THEIR COMPANY.

```html
<!DOCTYPE html>
<html lang="en">
<head>
<meta charset="utf-8">
<title>Permitronics – State Licenses for Builders and Electricians</title>
<link href="https://fonts.googleapis.com/css2?family=Poppins:wght@400;500;600;700&display=swap" rel="stylesheet">
<style>
:root{
  --teal:#13b9a5;
  --teal-dark:#0e9c8c;
  --blue:#0a8fd6;
  --ink:#222222;
  --body:#444444;
  --muted:#8a8a8a;
  --card-border:#ececec;
  --dark-band:#2e2e2e;
  --footer:#0b0b0b;
  --white:#ffffff;
  --star:#f3c31a;
}
*{box-sizing:border-box;margin:0;padding:0}
html,body{width:1200px;height:4275px;overflow:hidden}
body{font-family:'Poppins',sans-serif;color:var(--body);background:var(--white);position:relative}
.abs{position:absolute}
.logo{display:flex;align-items:center;gap:10px;color:var(--white);font-weight:500;font-size:24px}
.logo-dot{width:14px;height:14px;border-radius:50%;background:var(--teal)}

/* hero */
.hero{left:0;top:0;width:1200px;height:500px;overflow:hidden;
  background:linear-gradient(180deg,#3d2a1c 0%,#7a4f2e 35%,#a0683c 60%,#5a3a22 100%)}
.hero-photo{position:absolute;inset:0;background:radial-gradient(ellipse at 50% 60%,rgba(200,110,60,.55),rgba(30,20,15,.2) 70%)}
.hero .logo{position:absolute;left:110px;top:44px}
.nav{position:absolute;left:518px;top:34px;display:flex;gap:38px;font-size:14px;color:rgba(255,255,255,.85)}
.nav .active{color:var(--white);font-weight:500}
.btn-quote{position:absolute;left:965px;top:26px;width:124px;height:42px;border-radius:21px;background:var(--teal);
  color:var(--white);font-size:15px;font-weight:500;display:flex;align-items:center;justify-content:center}
.hero-title{position:absolute;left:0;top:278px;width:1200px;text-align:center;color:var(--white);font-size:48px;line-height:70px;font-weight:400}
.hero-title b{font-weight:700}
.arrow-btn{position:absolute;width:28px;height:28px}

/* section headings */
.h2{position:absolute;left:0;width:1200px;text-align:center;font-size:33px;font-weight:600;color:var(--ink)}
.h2 .bar{position:absolute;height:3px;background:var(--teal)}

/* about */
.about-title{left:112px;top:600px;font-size:33px;font-weight:600;color:var(--ink)}
.about-text{left:112px;top:680px;width:520px;font-size:15px;line-height:28px}
.about-text p{margin-bottom:17px}
.btn{display:flex;align-items:center;justify-content:center;border-radius:22px;color:var(--white);font-weight:500}
.about-photo{left:690px;top:600px;width:402px;height:402px;border-radius:50%;
  background:linear-gradient(135deg,#8aa1b8,#c9b79a 55%,#5f6f80)}
.about-blob{left:744px;top:905px;width:118px;height:118px;border-radius:50%;background:rgba(19,185,165,.85)}

/* services */
.services-desc{left:200px;top:1200px;width:800px;text-align:center;font-size:15px;line-height:28px}
.service-card{position:absolute;top:1362px;width:294px;height:344px;border:1px solid var(--card-border);border-radius:10px;background:var(--white);
  box-shadow:0 4px 14px rgba(0,0,0,.05);text-align:center;padding:75px 32px 0}
.service-card h3{font-size:20px;font-weight:500;color:var(--ink);line-height:33px;margin-bottom:14px}
.service-card p{font-size:14px;line-height:28px}
.service-icon{position:absolute;left:97px;top:-50px;width:100px;height:100px;border-radius:50%;border:4px solid var(--teal);background:var(--white);
  display:flex;align-items:center;justify-content:center}
.service-card .btn{position:absolute;left:80px;bottom:-20px;width:134px;height:38px;font-size:14px;background:var(--teal)}
.service-card.blue .service-icon{border-color:var(--blue)}
.service-card.blue .btn{background:var(--blue)}

/* stats */
.stats{left:0;top:1832px;width:1200px;height:223px;background:linear-gradient(90deg,#2a2a2a,#3a3a3a 50%,#2a2a2a)}
.stat{position:absolute;top:64px;width:390px;text-align:center;color:var(--white)}
.stat .num{font-size:52px;font-weight:600;color:var(--teal);line-height:60px}
.stat .lbl{font-size:17px;font-weight:500;margin-top:8px}
.stat-divider{position:absolute;top:50px;width:1px;height:122px;background:rgba(255,255,255,.25)}

/* testimonials */
.map-circle{left:110px;top:2238px;width:480px;height:480px;border-radius:50%;background:#f6f6f6;border:8px solid #fafafa}
.map-area{left:175px;top:2360px;width:280px;height:280px;border-radius:12px;background:linear-gradient(135deg,#2a8fe0,#0f74c8)}
.map-logo{left:172px;top:2535px;display:flex;align-items:center;gap:8px;color:#555;font-size:22px;font-weight:500}
.testi-card{position:absolute;top:2305px;width:294px;height:345px;border:1px solid var(--card-border);border-radius:8px;background:var(--white);
  box-shadow:0 4px 14px rgba(0,0,0,.05);text-align:center;padding-top:45px}
.testi-card .q{position:absolute;font-size:60px;line-height:60px;color:var(--teal);font-weight:700}
.testi-card .name{font-size:19px;font-weight:500;color:var(--ink)}
.testi-card .role{font-size:15px;color:var(--muted)}
.testi-card .stars{color:var(--star);font-size:22px;letter-spacing:2px;margin:8px 0 10px}
.testi-card p{font-size:14px;line-height:28px;padding:0 32px}

/* blog */
.blog-card{position:absolute;top:2910px;width:307px;height:462px;border:1px solid var(--card-border);border-radius:6px;background:var(--white);
  box-shadow:0 4px 14px rgba(0,0,0,.05);overflow:visible}
.blog-img{width:100%;height:197px;border-radius:6px 6px 0 0}
.blog-avatar{position:absolute;left:15px;top:180px;width:62px;height:62px;border-radius:50%;border:3px solid var(--white);background:#b7a593}
.blog-author{position:absolute;left:86px;top:210px;font-size:15px;color:var(--muted)}
.blog-card h3{position:absolute;left:20px;top:270px;width:270px;font-size:17px;font-weight:500;color:var(--ink);line-height:26px}
.blog-card p{position:absolute;left:20px;top:324px;width:275px;font-size:14px;line-height:27px}
.blog-more{position:absolute;left:22px;top:420px;display:flex;align-items:center;gap:4px;color:var(--teal);font-size:13px}
.blog-more .ln{width:40px;height:1px;background:var(--teal)}

/* contact */
.footer{left:0;top:3690px;width:1200px;height:585px;background:var(--footer)}
.help{left:134px;top:3452px;width:932px;height:458px;border-radius:40px;background:linear-gradient(135deg,#13b9a5,#0a9ed0 60%,#0a8fd6)}
.help h2{position:absolute;top:46px;width:100%;text-align:center;color:var(--white);font-size:32px;font-weight:600}
.field{position:absolute;background:var(--white);border-radius:3px;font-size:15px;color:#444;padding:14px 20px}
.btn-submit{position:absolute;left:393px;top:376px;width:124px;height:42px;border:2px solid var(--white);border-radius:21px;color:var(--white);
  font-size:15px;font-weight:500;display:flex;align-items:center;justify-content:center}

/* footer */
.footer-logo{left:110px;top:4046px;display:flex;align-items:center;gap:10px;color:var(--white);font-size:30px;font-weight:500}
.f-col{position:absolute;top:4008px;color:var(--white)}
.f-col h4{font-size:15px;font-weight:500;letter-spacing:.5px;margin-bottom:14px}
.f-col li{list-style:none;font-size:16px;line-height:30px;display:flex;align-items:center;gap:10px;color:#e6e6e6}
.chev{color:var(--teal);font-size:14px}
.f-contact li{align-items:flex-start;margin-bottom:8px}
.f-rule{left:110px;top:4218px;width:980px;height:1px;background:#333}
.copyright{left:0;top:4238px;width:1200px;text-align:center;color:#e6e6e6;font-size:15px}
</style>
</head>
<body>

<header class="abs hero">
  <div class="hero-photo" role="img" aria-label="Photo of a construction worker in hard hat and safety vest facing a building site at sunset"></div>
  <div class="logo"><span class="logo-dot"></span>Permitronics</div>
  <nav class="nav"><span class="active">Home</span><span>About</span><span>Services</span><span>Blog</span><span>Contact</span></nav>
  <div class="btn-quote">Get Quote</div>
  <svg class="arrow-btn" style="left:39px;top:213px" viewBox="0 0 28 28"><circle cx="14" cy="14" r="12" fill="none" stroke="rgba(255,255,255,.6)" stroke-width="1.5"/><path d="M19 14H9M13 10l-4 4 4 4" fill="none" stroke="rgba(255,255,255,.6)" stroke-width="1.5"/></svg>
  <svg class="arrow-btn" style="left:1131px;top:213px" viewBox="0 0 28 28"><circle cx="14" cy="14" r="12" fill="none" stroke="#fff" stroke-width="1.5"/><path d="M9 14h10M15 10l4 4-4 4" fill="none" stroke="#fff" stroke-width="1.5"/></svg>
  <h1 class="hero-title">State Licenses for <b>Builders</b><br><b>and Electricians</b></h1>
  <svg style="position:absolute;left:0;top:440px" width="1200" height="60" viewBox="0 0 1200 60">
    <path d="M0 30 Q300 55 650 50 T1200 10 V60 H0Z" fill="#fff"/>
    <path d="M0 30 Q250 50 560 48" fill="none" stroke="#0a8fd6" stroke-width="10"/>
    <path d="M660 50 Q950 45 1200 8" fill="none" stroke="#13b9a5" stroke-width="8"/>
  </svg>
</header>

<section>
  <h2 class="abs about-title">ABOUT US<span class="abs" style="left:125px;top:45px;width:30px;height:3px;background:var(--teal)"></span></h2>
  <div class="abs about-text">
    <p>Sed ut perspiciatis unde omnis uptatem accusantium doloremque laudantium, totam rem aperiam, eaque ipsa quae ab illo inventore veritatis et quasi architecto atae viae dicta sunt explicabo. Nemo enim ipsam voluptatem quia voptas sit aspernatur aut odit aut fugit, sed quia consequuntur mdolores eos qui ratione voluptatem sequi nesciunt. Neque porro quisquam est, qui dolorem ipsum</p>
    <p>Lorem ipsum dolor sit amet, conser adipiscing elit, sed do eiusmod tempor incididunt ut labore etagn aliqua. Quis ipsum suspendisse ultrices gravida.</p>
  </div>
  <div class="abs btn" style="left:112px;top:986px;width:123px;height:43px;background:var(--teal);font-size:15px">Learn More</div>
  <div class="abs about-photo" role="img" aria-label="Photo of a smiling contractor in a plaid shirt with a tool belt in a workshop"></div>
  <div class="abs about-blob"></div>
</section>

<section>
  <h2 class="h2" style="top:1122px">OUR SERVICES<span class="bar" style="left:668px;top:48px;width:68px"></span></h2>
  <p class="abs services-desc">Lorem ipsum dolor sit amet, conser adipiscing elit, sed do eiusmod tempor incididunt ut labore etagn aliqua. Quis ipsum suspendisse ultrices gravida.</p>
  <svg class="arrow-btn" style="left:39px;top:1504px" viewBox="0 0 28 28"><circle cx="14" cy="14" r="12" fill="none" stroke="#bbb" stroke-width="1.5"/><path d="M19 14H9M13 10l-4 4 4 4" fill="none" stroke="#bbb" stroke-width="1.5"/></svg>
  <svg class="arrow-btn" style="left:1131px;top:1504px" viewBox="0 0 28 28"><circle cx="14" cy="14" r="12" fill="none" stroke="#222" stroke-width="1.5"/><path d="M9 14h10M15 10l4 4-4 4" fill="none" stroke="#222" stroke-width="1.5"/></svg>

  <div class="service-card" style="left:112px">
    <div class="service-icon"><svg width="44" height="44" viewBox="0 0 44 44" fill="none" stroke="#333" stroke-width="2"><path d="M20 4l14 5v11c0 9-6 15-14 18C12 35 6 29 6 20V9z"/><circle cx="20" cy="17" r="4"/><path d="M13 28c1-5 13-5 14 0"/><circle cx="33" cy="32" r="6"/><path d="M30 32l2 2 4-4"/></svg></div>
    <h3>Initial application for licensure</h3>
    <p>Lorem ipsum dimet, consecter adipiscing elit, sed do eiusmod tempor incididunt ut labore et dolore magna aua. Quis ipsum suspendisse ultrices gravida.</p>
    <div class="btn">Learn More</div>
  </div>
  <div class="service-card blue" style="left:453px">
    <div class="service-icon"><svg width="44" height="44" viewBox="0 0 44 44" fill="none" stroke="#333" stroke-width="2"><rect x="8" y="6" width="24" height="32" rx="2"/><path d="M13 14h14M13 20h10M13 26h8"/><circle cx="32" cy="28" r="5"/><path d="M30 33l-1 6 3-2 3 2-1-6"/></svg></div>
    <h3>Additional<br>Licensure</h3>
    <p>Lorem ipsum dimet, consecter adipiscing elit, sed do eiusmod tempor incididunt ut labore et dolore magna aua. Quis ipsum suspendisse ultrices gravida.</p>
    <div class="btn">Learn More</div>
  </div>
  <div class="service-card" style="left:794px">
    <div class="service-icon"><svg width="44" height="44" viewBox="0 0 44 44" fill="none" stroke="#333" stroke-width="2"><rect x="5" y="12" width="34" height="24" rx="2"/><rect x="16" y="7" width="12" height="8" rx="1"/><circle cx="14" cy="22" r="3"/><path d="M9 31c1-4 9-4 10 0M23 21h11M23 26h11M23 31h8"/></svg></div>
    <h3>License<br>Probation</h3>
    <p>Lorem ipsum dimet, consecter adipiscing elit, sed do eiusmod tempor incididunt ut labore et dolore magna aua. Quis ipsum suspendisse ultrices gravida.</p>
    <div class="btn">Learn More</div>
  </div>
</section>

<section class="abs stats" aria-label="Key figures">
  <div class="stat" style="left:20px"><div class="num">150%</div><div class="lbl">Overall Growth</div></div>
  <div class="stat-divider" style="left:389px"></div>
  <div class="stat" style="left:392px"><div class="num">15,000</div><div class="lbl">Licenses Provided</div></div>
  <div class="stat-divider" style="left:776px"></div>
  <div class="stat" style="left:780px"><div class="num">10,500</div><div class="lbl">Terminate Probation</div></div>
</section>

<section>
  <h2 class="h2" style="top:2143px">CLIENT TESTIMONIALS<span class="bar" style="left:734px;top:48px;width:66px"></span></h2>
  <div class="abs map-circle"></div>
  <div class="abs map-area" style="height:170px" role="img" aria-label="Map of Florida counties"></div>
  <div class="abs map-logo"><span class="logo-dot"></span>Permitronics</div>

  <div class="testi-card" style="left:477px">
    <span class="q" style="left:26px;top:8px">“</span>
    <div class="name">Dana R</div><div class="role">Lorem Ipsum</div>
    <div class="stars">★★★★★</div>
    <p>Lorem ipsum dimet, consecter adipiscing elit, sed do eiusmod tempor incididunt ut labore et dolore magna aua. Quis ipsum suspendisse ultrices gravida.</p>
    <span class="q" style="right:22px;bottom:-18px">”</span>
  </div>
  <div class="testi-card" style="left:796px">
    <span class="q" style="left:26px;top:8px">“</span>
    <div class="name">Dana R</div><div class="role">Lorem Ipsum</div>
    <div class="stars">★★★★★</div>
    <p>Lorem ipsum dimet, consecter adipiscing elit, sed do eiusmod tempor incididunt ut labore et dolore magna aua. Quis ipsum suspendisse ultrices gravida.</p>
    <span class="q" style="right:22px;bottom:-18px">”</span>
  </div>
</section>

<section>
  <h2 class="h2" style="top:2788px">LATEST BLOG<span class="bar" style="left:654px;top:48px;width:66px"></span></h2>

  <article class="blog-card" style="left:112px">
    <div class="blog-img" role="img" aria-label="Photo of two electricians standing by a work van" style="background:linear-gradient(135deg,#7fa6cc,#d9dde2 55%,#3d5673)"></div>
    <div class="blog-avatar" role="img" aria-label="Author portrait"></div>
    <span class="blog-author">Lorem Ipsum</span>
    <h3>Sed ut perspiciatis unde omnis iste natus error sit</h3>
    <p>Sed ut perspiciatis unde omnis iste natus err sit Sed ut persiatis unde omnis iste natus error sit.</p>
    <div class="blog-more"><span class="ln"></span>MORE<span>⟶</span></div>
  </article>
  <article class="blog-card" style="left:447px">
    <div class="blog-img" role="img" aria-label="Photo of a worker in a hard hat overlooking a city at sunset" style="background:linear-gradient(180deg,#3a4a66,#c77a45 60%,#4a2f22)"></div>
    <div class="blog-avatar" role="img" aria-label="Author portrait"></div>
    <span class="blog-author">Lorem Ipsum</span>
    <h3>Sed ut perspiciatis unde omnis iste natus error sit</h3>
    <p>Sed ut perspiciatis unde omnis iste natus err sit Sed ut persiatis unde omnis iste natus error sit.</p>
    <div class="blog-more"><span class="ln"></span>MORE<span>⟶</span></div>
  </article>
  <article class="blog-card" style="left:782px">
    <div class="blog-img" role="img" aria-label="Photo of an architectural building model on blueprints" style="background:linear-gradient(135deg,#e8e8e8,#a9a9a9 60%,#cfcfcf)"></div>
    <div class="blog-avatar" role="img" aria-label="Author portrait"></div>
    <span class="blog-author">Lorem Ipsum</span>
    <h3>Sed ut perspiciatis unde omnis iste natus error sit</h3>
    <p>Sed ut perspiciatis unde omnis iste natus err sit Sed ut persiatis unde omnis iste natus error sit.</p>
    <div class="blog-more"><span class="ln"></span>MORE<span>⟶</span></div>
  </article>
</section>

<footer class="abs footer"></footer>

<section class="abs help">
  <h2>HOW CAN WE HELP YOU?</h2>
  <div class="field" style="left:126px;top:121px;width:332px;height:47px">Name</div>
  <div class="field" style="left:472px;top:121px;width:332px;height:47px">Email</div>
  <div class="field" style="left:126px;top:186px;width:332px;height:47px">Phone</div>
  <div class="field" style="left:472px;top:186px;width:332px;height:47px">Subject</div>
  <div class="field" style="left:126px;top:250px;width:678px;height:95px">Message</div>
  <div class="btn-submit">Submit</div>
</section>

<div class="abs footer-logo"><span class="logo-dot" style="width:16px;height:16px"></span>Permitronics</div>
<div class="f-col" style="left:410px">
  <h4>QUICK LINKS</h4>
  <ul><li><span class="chev">»</span>Home</li><li><span class="chev">»</span>About</li><li><span class="chev">»</span>Services</li><li><span class="chev">»</span>Blog</li></ul>
</div>
<div class="f-col f-contact" style="left:616px">
  <h4>CONTACT</h4>
  <ul>
    <li><svg width="18" height="20" viewBox="0 0 18 20"><path d="M9 1a6 6 0 0 1 6 6c0 5-6 12-6 12S3 12 3 7a6 6 0 0 1 6-6z" fill="#fff"/><circle cx="9" cy="7" r="2.3" fill="#0b0b0b"/></svg><span>Permitronics,<br>Address comes here</span></li>
    <li><svg width="18" height="18" viewBox="0 0 24 24"><path d="M6.6 10.8a15 15 0 0 0 6.6 6.6l2.2-2.2c.3-.3.7-.4 1-.2 1.1.4 2.3.6 3.6.6.6 0 1 .4 1 1V20c0 .6-.4 1-1 1A17 17 0 0 1 3 4c0-.6.4-1 1-1h3.5c.6 0 1 .4 1 1 0 1.3.2 2.5.6 3.6.1.3 0 .7-.2 1z" fill="#fff"/></svg>+1-800-555-0142</li>
    <li><svg width="18" height="18" viewBox="0 0 24 24"><rect x="2" y="5" width="20" height="14" rx="1" fill="#fff"/><path d="M2 6l10 7 10-7" fill="none" stroke="#0b0b0b" stroke-width="1.6"/></svg>info@permitronics.com</li>
  </ul>
</div>
<div class="f-col" style="left:898px">
  <h4>OTHER LINKS</h4>
  <ul><li><span class="chev">»</span>Tearms &amp; Condition</li><li><span class="chev">»</span>Privacy Policy</li><li><span class="chev">»</span>Contact</li></ul>
</div>
<div class="abs f-rule"></div>
<p class="abs copyright">2023 Permitronics. All Rights Reserved.</p>

</body>
</html>
```